Healthcare technology firm needs business card layout. Logo provided.

We need a business card design for a new healthcare technology company called Mirvela.com. The logo is already done so that will be used in the design. We assist patients and their families manage their personal health finances. Our initial product is our web site membership that includes educational content on your health benefits, tools, and downloadable forms.

We would like to see designs that use our existing logo or extend the logo in a creative way. Should be very consumer friendly.

```html
<!DOCTYPE html>
<html lang="en">
<head>
<meta charset="utf-8">
<title>Mirvela Business Card</title>
<link href="https://fonts.googleapis.com/css2?family=Questrial&family=Mulish:wght@700&display=swap" rel="stylesheet">
<style>
  :root {
    --page: #ffffff;
    --card: #ffffff;
    --brand-blue: #0a3cf0;
    --brand-green: #2ee84a;
    --ink: #111111;
    --band-start: #2ee84a;
    --band-mid: #1e7fb0;
    --band-end: #0a3cff;
    --on-band: #ffffff;
  }
  html, body {
    margin: 0;
    width: 1200px;
    height: 900px;
    overflow: hidden;
    background: var(--page);
    font-family: "Questrial", "Century Gothic", sans-serif;
  }
  .business-card {
    position: absolute;
    left: 66px;
    top: 119px;
    width: 1063px;
    height: 650px;
    background: var(--card);
    box-shadow: 2px 3px 5px rgba(0, 0, 0, 0.18);
  }
  .brand {
    position: absolute;
    left: 54px;
    top: 46px;
    display: flex;
    align-items: center;
    gap: 14px;
  }
  .brand-name {
    font-size: 96px;
    line-height: 1;
    letter-spacing: 3px;
    color: var(--brand-blue);
  }
  .brand-dot {
    width: 22px;
    height: 22px;
    border-radius: 50%;
    background: var(--brand-green);
    margin-top: 40px;
  }
  .tagline {
    position: absolute;
    right: 582px;
    top: 179px;
    margin: 0;
    text-align: right;
    font-style: italic;
    font-size: 25px;
    line-height: 29px;
    color: var(--brand-blue);
  }
  .contact {
    position: absolute;
    right: 59px;
    top: 206px;
    text-align: right;
    color: var(--ink);
  }
  .person-name {
    margin: 0 0 34px;
    font-family: "Mulish", "Century Gothic", sans-serif;
    font-weight: 700;
    font-size: 36px;
    line-height: 44px;
    color: var(--brand-blue);
  }
  .person-title {
    font-family: "Questrial", "Century Gothic", sans-serif;
    font-weight: 400;
    font-size: 24px;
    margin-left: 8px;
  }
  .address {
    margin: 0 0 18px;
    font-style: normal;
    font-size: 29px;
    line-height: 41px;
  }
  .phone-list {
    list-style: none;
    margin: 0;
    padding: 0;
    font-size: 29px;
    line-height: 41px;
  }
  .phone-list li {
    display: flex;
    justify-content: flex-end;
    align-items: center;
    gap: 9px;
  }
  .phone-icon { width: 30px; height: 26px; }
  .office-band {
    position: absolute;
    left: 0;
    top: 499px;
    width: 100%;
    height: 71px;
    background: linear-gradient(90deg, var(--band-start) 0%, var(--band-mid) 34%, var(--band-end) 70%, var(--band-end) 100%);
    display: flex;
    align-items: center;
    padding-left: 160px;
    gap: 46px;
    box-sizing: border-box;
  }
  .office {
    color: var(--on-band);
    font-size: 33px;
  }
</style>
</head>
<body>
  <article class="business-card">
    <div class="brand">
      <span class="brand-name">MIRVELA</span>
      <span class="brand-dot"></span>
    </div>
    <p class="tagline">Making your care<br>make sense</p>

    <div class="contact">
      <h1 class="person-name">Dana R. Whitfield<span class="person-title">CEO</span></h1>
      <address class="address">4120 Corvane Way, Suite 210,<br>Calder Springs, FL 33907</address>
      <ul class="phone-list">
        <li>
          <svg class="phone-icon" viewBox="0 0 30 26" aria-label="Phone">
            <path d="M2 9 Q15 0 28 9 L25 12 L21 10 L20 7 Q15 5 10 7 L9 10 L5 12 Z" fill="#111"/>
            <path d="M8 12 L22 12 L27 22 L3 22 Z" fill="#111"/>
            <circle cx="15" cy="17" r="3" fill="#fff"/>
          </svg>
          <span>239-555-0142</span>
        </li>
        <li>
          <svg class="phone-icon" viewBox="0 0 30 26" aria-label="Fax">
            <rect x="8" y="1" width="14" height="12" fill="none" stroke="#111" stroke-width="2"/>
            <line x1="11" y1="5" x2="19" y2="5" stroke="#111" stroke-width="1.5"/>
            <line x1="11" y1="9" x2="19" y2="9" stroke="#111" stroke-width="1.5"/>
            <path d="M3 14 Q15 9 27 14 L27 24 L3 24 Z" fill="none" stroke="#111" stroke-width="2"/>
            <line x1="7" y1="19" x2="23" y2="19" stroke="#111" stroke-width="1.5"/>
          </svg>
          <span>636-555-0178</span>
        </li>
      </ul>
    </div>

    <div class="office-band">
      <span class="office">Brightwater</span>
      <span class="office">Calder Springs</span>
      <span class="office">Mesa Vale</span>
      <span class="office">Port Avenell</span>
    </div>
  </article>
</body>
</html>
```